Lotuvan Cafe Menu rev.01

Design an elegant menu for Khmer restaurant in Melbourne.

-Size and format can be proposed (not bigger than A3)
-Food and beverages split (separate sides of the menu)
-Sample excel file - Food attached
-Sample Menu Pdf attached (just to get an idea)
-Details shall be reviewed and considered
-Prices in AUD
-Easy to print and clean (format need to to printable)
-Provision for future updates.

If you have any further question please let us know.
Regards,

Dexter

Target Market(s)

Customers win the restaurant

Industry/Entity Type

Hospitality - Restaurant

Colors

Designer to choose colors to be used in the design.

Requirements
Must have
• Authentic touch - clear structure
Nice to have
• Welcome about the restaurant. Complete information - see sample menu

```html
<!DOCTYPE html>
<html lang="en">
<head>
<meta charset="utf-8">
<title>Lotuvan Cafe – Food Menu</title>
<link href="https://fonts.googleapis.com/css2?family=Oswald:wght@500&family=Montserrat:wght@400;600;700&display=swap" rel="stylesheet">
<style>
  :root{
    --ink:#111111;
    --paper:#ecebe8;
    --paper-dark:#dddcd8;
    --gold:#c2ae79;
    --line:#2a2a2a;
    --leaf:#b7c6aa;
    --leaf-soft:#dde3d6;
    --bloom:#d8457a;
    --bloom-soft:#e7a3bb;
    --photo-green:#4d7a62;
    --photo-warm:#c08a5e;
    --frame:#ffffff;
  }
  *{box-sizing:border-box;margin:0;padding:0}
  html,body{width:977px;height:1200px;overflow:hidden;background:var(--paper)}
  .menu{
    position:relative;width:977px;height:1200px;overflow:hidden;
    background:radial-gradient(ellipse at 40% 45%, #f4f3f1 0%, var(--paper) 55%, var(--paper-dark) 100%);
    font-family:"Montserrat",sans-serif;color:var(--ink);
  }
  .header-band{position:absolute;left:0;top:0;width:977px;height:172px;background:var(--ink)}
  .art{position:absolute}
  .art--foliage-left{left:240px;top:172px;width:150px;height:150px;background:linear-gradient(180deg,var(--leaf-soft),rgba(221,227,214,0));}
  .art--foliage-right{left:590px;top:172px;width:150px;height:140px;background:linear-gradient(180deg,var(--leaf-soft),rgba(221,227,214,0));}
  .brand-seal{
    position:absolute;left:360px;top:40px;width:260px;height:260px;border-radius:50%;
    background:var(--ink);display:flex;align-items:center;justify-content:center;
  }
  .brand-name{
    font-family:"Oswald",sans-serif;font-weight:500;color:var(--gold);
    font-size:40px;letter-spacing:2px;text-transform:uppercase;line-height:1;text-align:center;
  }
  .section{position:absolute;border:1.5px solid var(--line)}
  .section--bites{left:29px;top:380px;width:449px;height:334px}
  .section--dish{left:497px;top:380px;width:449px;height:435px}
  .section--khmer{left:29px;top:770px;width:449px;height:277px}
  .section-tab{
    position:absolute;left:17px;top:-26px;height:51px;background:var(--ink);
    color:var(--gold);font-family:"Oswald",sans-serif;font-weight:500;font-size:27px;
    line-height:51px;padding:0 34px 0 14px;text-transform:uppercase;letter-spacing:0.2px;
    clip-path:polygon(0 0, calc(100% - 28px) 0, 100% 100%, 0 100%);
    transform:scaleX(0.88);transform-origin:left center;white-space:nowrap;
  }
  .dish{position:absolute;left:17px;right:17px}
  .dish-name{font-weight:700;font-size:12.5px;line-height:14px;text-transform:uppercase;letter-spacing:0.2px}
  .dish-desc{font-size:9.2px;line-height:11px;width:270px;margin-top:0}
  .dish-price{position:absolute;right:0;top:0;font-weight:600;font-size:13px;line-height:14px}
  .notes-rule{position:absolute;left:29px;top:1084px;width:497px;height:1px;background:var(--line)}
  .notes{position:absolute;left:29px;top:1111px;list-style:none;font-size:11.3px;line-height:14.6px}
  .notes li::before{content:"· "}
  .art--leaves{left:745px;top:790px;width:232px;height:410px;background:linear-gradient(180deg,var(--leaf-soft),var(--leaf));}
  .art--flower{left:545px;top:990px;width:170px;height:190px;background:linear-gradient(160deg,var(--bloom-soft),var(--bloom));}
  .art--photo-small{left:640px;top:835px;width:166px;height:166px;border-radius:50%;border:7px solid var(--frame);background:var(--photo-green)}
  .art--photo-large{left:690px;top:947px;width:250px;height:250px;border-radius:50%;border:7px solid var(--frame);background:linear-gradient(160deg,#d8b38c,var(--photo-warm))}
</style>
</head>
<body>
<main class="menu">
  <div class="header-band"></div>
  <div class="art art--foliage-left" role="img" aria-label="Watercolour leaves"></div>
  <div class="art art--foliage-right" role="img" aria-label="Watercolour leaves"></div>
  <div class="brand-seal"><span class="brand-name">Lotuvan Cafe</span></div>

  <section class="section section--bites">
    <h2 class="section-tab">Tasty Bites</h2>
    <div class="dish" style="top:60px"><div class="dish-name">Betel Leaf</div><p class="dish-desc" style="width:262px">A traditional Cambodian appetizer, betel leafs with Asian Pomegranate, prawns, herbs and special Lotuvan sauce with a dust of peanuts or coconut shredded (1 pcs)</p><span class="dish-price">$ 4.50</span></div>
    <div class="dish" style="top:132px"><div class="dish-name">Crispy Sweet Potatoes</div><p class="dish-desc" style="width:262px">Fritted finger strips of sweet potatoes served in a bowl</p><span class="dish-price">$ 6.00</span></div>
    <div class="dish" style="top:184px"><div class="dish-name">Spring Rolls</div><p class="dish-desc" style="width:330px">Deep fired roll with pork and prawns, vegetable (3 pcs)</p><span class="dish-price">$ 10.20</span></div>
    <div class="dish" style="top:225px"><div class="dish-name">Vegetarian Spring Rolls</div><p class="dish-desc">Deep fired roll, vegetable (3 pcs)</p><span class="dish-price">$ 9.00</span></div>
    <div class="dish" style="top:265px"><div class="dish-name">BBQ Scallop</div><p class="dish-desc" style="width:262px">Sea scallop with herbs and special Lotuvan dressing (2 pcs)</p><span class="dish-price">$ 10.00</span></div>
  </section>

  <section class="section section--dish">
    <h2 class="section-tab">Lotuvan Dish</h2>
    <div class="dish" style="top:60px"><div class="dish-name">Fish Amok</div><p class="dish-desc">Traditional Cambodian Dish in a banana leaf, Markel fish, curry paste, coconut, Chinese Broccoli served with Jasmine rice</p><span class="dish-price">$ 27.00</span></div>
    <div class="dish" style="top:121px"><div class="dish-name">Red Curry</div><p class="dish-desc">Red Curry with chicken &amp; vegetable</p><span class="dish-price">$ 17.00</span></div>
    <div class="dish" style="top:160px"><div class="dish-name">Green Curry</div><p class="dish-desc">Green Curry with Beef or Fish (Markel filet), with pineapple, eggplant &amp; bamboo</p><span class="dish-price">$ 17.00</span></div>
    <div class="dish" style="top:213px"><div class="dish-name">Kampot Pepper with Seafood</div><p class="dish-desc">Kampot Pepper with Seafood, onion, carrot &amp; dust of Spring onion</p><span class="dish-price">$ 25.00</span></div>
    <div class="dish" style="top:269px"><div class="dish-name">Char Kreung Chicken or Fish</div><p class="dish-desc">Stirred-fried of commination chicken or fish, mix vegetable, green beans, sweet chilli</p><span class="dish-price">$ 22.00</span></div>
    <div class="dish" style="top:325px"><div class="dish-name">Beef Loc Lac</div><p class="dish-desc">Cambodian marinated beef chunks and vegetable served with crispy sweet potato strips</p><span class="dish-price">$ 24.50</span></div>
    <div class="dish" style="top:381px"><div class="dish-name">Traditional Lotuvan Soup</div><p class="dish-desc" style="width:235px">A mild spicy sweet and sour soup with fish &amp; mushrooms</p><span class="dish-price">$ 21.00</span></div>
  </section>

  <section class="section section--khmer">
    <h2 class="section-tab">Khmer Breakfast or Lunch</h2>
    <div class="dish" style="top:60px"><div class="dish-name">Kuy Teav Phnom Penh</div><p class="dish-desc" style="width:245px">Traditional Cambodian noodle soup, rice and yellow noodles, choice of Pork, Beef or Seafood</p><span class="dish-price">$ 15.50</span></div>
    <div class="dish" style="top:114px"><div class="dish-name">Lot Cha</div><p class="dish-desc">Rice drop noodles with Chinese chives, bean sprouts, chicken, beef ham and a dust of special Lotuvan sauce</p><span class="dish-price">$ 14.50</span></div>
    <div class="dish" style="top:164px"><div class="dish-name">Kuy Teav Char</div><p class="dish-desc" style="width:262px">Stir-fired rice noodles, minced pork, ham, egg, bean sprouts and peanut sauce</p><span class="dish-price">$ 14.80</span></div>
    <div class="dish" style="top:216px"><div class="dish-name">Lemongrass Fried Rice</div><p class="dish-desc" style="width:235px">Lemongrass, onion, chicken or beef carrot and French beans</p><span class="dish-price">$ 16.50</span></div>
  </section>

  <div class="art art--leaves" role="img" aria-label="Watercolour tropical leaves"></div>
  <div class="art art--flower" role="img" aria-label="Pink flower illustration"></div>
  <div class="art art--photo-small" role="img" aria-label="Photo of a plated dish on a green leaf"></div>
  <div class="art art--photo-large" role="img" aria-label="Photo of grilled chicken with rice and salad"></div>

  <div class="notes-rule"></div>
  <ul class="notes">
    <li>10% surcharge on public holiday</li>
    <li>All prices are included GST</li>
    <li>All prices are subject to be change without prior notice</li>
    <li>If you are concerned with allergies to certain ingredients please inform our staff.</li>
    <li>Food ingredients and prices are subject to be changed without prior notice</li>
  </ul>
</main>
</body>
</html>
```